Business Card Design Project

I need a business card designed that is clean, simple and elegant.
I am a fashion and advertising photographer based in Cape Town and Durban South Africa.
check out my website: www.brennowalsh.co.za for ideas
Updates
Hi all,
Thanks for your submissions so far!
Please note:
I want no more than than black, white and/or grey to be used.
I don't want any photos used.
I would like the card to be double sided.
I would like to continue the design similar to the past ones Ive used.
I hope this helps, please send me further questions should you have any.
many thanks!
Brenno
Hi,
Please have a look at the jpg I loaded(called inspiration) which is the direction or inspiration I am aiming at.
Also PLEASE remember NO PHOTOS to be included on the card
many thanks!!
Target Market(s)
You can look at my site to get a better understanding of the audience:
www.brennowalsh.co.za
Industry/Entity Type
Advertising
Requirements
Must have
- Clean design which can also be used for a watermark on photographs
perhaps black background with white text/grey
company called: Brenno Walsh Photography
Nice to have
- below I have added logos that I have used in the past.
Should not have
- pictures of cameras
tacky elements

```html
<!DOCTYPE html>
<html lang="en">
<head>
<meta charset="utf-8">
<title>Brenno Walsh Photography – Business Card, Front and Back</title>
<link rel="stylesheet" href="https://fonts.googleapis.com/css2?family=Orbitron:wght@400;500&display=swap">
<style>
  :root {
    --backdrop: #d8d4cd;
    --card-black: #060606;
    --card-edge: #1c1c1c;
    --text-light: #e8e8e8;
    --text-grey: #b4b4b4;
    --label-grey: #8a8a8a;
    --rule-grey: #555555;
  }
  html, body {
    margin: 0;
    padding: 0;
    width: 1200px;
    height: 1023px;
    overflow: hidden;
    background: var(--backdrop);
  }
  .canvas {
    width: 1200px;
    height: 1023px;
    display: flex;
    flex-direction: column;
    align-items: center;
    justify-content: center;
    gap: 40px;
  }
  .business-card {
    position: relative;
    width: 760px;
    height: 434px;
    background: var(--card-black);
    border: 1px solid var(--card-edge);
    border-radius: 4px;
    box-shadow: 0 14px 32px rgba(0, 0, 0, 0.3);
    font-family: "Orbitron", sans-serif;
    overflow: hidden;
  }
  .contact-block {
    position: absolute;
    left: 380px;
    top: 110px;
    padding-left: 16px;
    border-left: 2px solid var(--rule-grey);
    display: flex;
    flex-direction: column;
    gap: 10px;
  }
  .contact-line {
    font-size: 14px;
    letter-spacing: 1px;
    color: var(--text-grey);
    text-transform: uppercase;
    white-space: nowrap;
  }
  .contact-label {
    color: var(--label-grey);
    margin-right: 6px;
  }
  .brand-name {
    margin: 0;
    font-weight: 500;
    color: var(--text-light);
    text-transform: uppercase;
    letter-spacing: 2px;
    line-height: 1.15;
  }
  .card-front .brand-name {
    position: absolute;
    left: 56px;
    top: 290px;
    font-size: 28px;
  }
  .card-back {
    display: flex;
    align-items: center;
    justify-content: center;
  }
  .card-back .brand-name {
    font-size: 40px;
    text-align: center;
  }
</style>
</head>
<body>
  <main class="canvas">
    <section class="business-card card-front" aria-label="Business card front">
      <div class="contact-block">
        <div class="contact-line"><span class="contact-label">E:</span>brenno@brennowalsh.co.za</div>
        <div class="contact-line"><span class="contact-label">P:</span>+27 (0)82 555 0147</div>
        <div class="contact-line"><span class="contact-label">W:</span>www.brennowalsh.co.za</div>
      </div>
      <h1 class="brand-name">Brenno Walsh<br>Photography</h1>
    </section>
    <section class="business-card card-back" aria-label="Business card back">
      <h2 class="brand-name">Brenno Walsh<br>Photography</h2>
    </section>
  </main>
</body>
</html>
```